Market Corner Fair needs a poster design

We need a poster to promote our showcase to both potential local vendors now, and visitors to the show on the actual day. See attached files and also checkout our Chatterbook page - "Market Corner Fair" for more information. Please state that booths are 8' (don't say 8' by 8'). See attached info that we have done so far, but we need something more professional. Ensure you use the Stay Bright Buy Nearby logo. The poster should be printable on both letter (8 1/2" by 11') and ledger sizes (11" by 17"). I have attached a sample of the poster from our last event - the Dwelling Expo 2013. I want the new poster similar to this (doesn't have to be exact, this is just to give you an idea.. The grand prize this time is a trip for two! The contact info has changed too, please note it on the new poster. I am no longer with my last company (UofW, Brantmoor Campus), so don't put that on the new poster. Thank you. You can email me with any questions. marketcornerfair@mailbay.example

Target Market(s)

Vendors for booth rentals. The community to visit the show.... They need to know that someone is going to win a trip for 2. We also have food, beer and wine sampling.

Industry/Entity Type

It Company

Font styles to use
Sans Serif

Requirements
Must have
• Stay bright buy nearby logo. Location. Email. Phone numbers. "Like our Chatterbook page - "Market Corner Fair". Poster is meant to attract business vendors now and to advertise the show to the public to attend in April. Must be able to print the poster on both letter size and ledger size paper. Need it in jpg too for Chatterbook uploads
Nice to have
• If it fits would be nice to say first of its kind in North Grenville
• First annual Market Corner Fair
Should not have
• Not too wordy.... Can't be confusing. Don't really need booth size on poster. Just state that both booths and marketplace tables are available. Not too many colours. We will be putting the poster in the newspaper in black and white only!

```html
<!DOCTYPE html>
<html lang="en">
<head>
<meta charset="utf-8">
<title>1st Annual Market Corner Fair</title>
<link rel="stylesheet" href="https://fonts.googleapis.com/css2?family=Montserrat:wght@400;600;700;800&family=Questrial&display=swap">
<style>
  :root{
    --ink:#1e1e1e;
    --band:#363636;
    --slogan-bg:#232323;
    --tag:#2a2a2a;
    --arrow:#111111;
    --white:#ffffff;
    --paper:#e9e9e6;
    --paper-dark:#d4d4d0;
    --field-light:#e6e6e6;
    --field-mid:#b9b9b9;
    --field-dark:#7a7a7a;
  }
  *{box-sizing:border-box;margin:0;padding:0}
  html,body{width:1089px;height:1200px;overflow:hidden}
  body{position:relative;font-family:"Questrial",Arial,sans-serif;color:var(--ink)}

  .newsprint-backdrop{
    position:absolute;inset:0;
    background:linear-gradient(180deg,var(--paper) 0%,var(--paper-dark) 100%);
  }

  .poster{
    position:absolute;left:118px;top:75px;width:824px;height:1062px;
    overflow:hidden;
    background:radial-gradient(ellipse 70% 60% at 50% 45%,var(--field-light) 0%,var(--field-mid) 55%,var(--field-dark) 100%);
  }

  .header-band{position:absolute;left:0;top:0;width:824px;height:210px;background:var(--band)}
  .slogan-block{position:absolute;left:0;top:0;width:300px;height:360px}

  .slogan{
    position:absolute;left:0;top:80px;width:252px;
    text-align:center;color:var(--white);
    font-family:"Montserrat",Arial,sans-serif;font-weight:700;
    line-height:1.02;text-transform:uppercase;
  }
  .slogan .big{display:block;font-size:40px;letter-spacing:.5px}
  .slogan .small{display:block;font-size:24px;margin:2px 0}

  .title{position:absolute;left:240px;top:40px;width:584px;text-align:center;color:var(--white);font-weight:normal}
  .title-year{display:block;font-family:"Questrial",Arial,sans-serif;font-size:60px;letter-spacing:5px;line-height:1}
  .title-name{display:block;font-family:"Montserrat",Arial,sans-serif;font-weight:700;font-size:41px;line-height:1.2;margin-top:6px}

  .tagline{position:absolute;left:384px;top:252px;font-size:22px;color:var(--ink)}

  .booth-visual{
    position:absolute;left:470px;top:324px;width:354px;height:470px;
    background:linear-gradient(160deg,#f2f2f2 0%,#d0d0d0 55%,#9a9a9a 100%);
  }

  .info-tag{position:absolute;left:0;height:54px;color:var(--white);font-size:22px;line-height:54px;padding-left:18px;font-weight:600}
  .info-tag svg{position:absolute;left:0;top:0}
  .info-tag span{position:relative}
  .tag-venue{top:403px;width:415px}
  .tag-date{top:466px;width:295px}
  .tag-hours{top:530px;width:195px;font-size:25px}

  .categories{position:absolute;left:28px;top:624px;list-style:none;font-size:24px;line-height:30px;color:var(--ink)}
  .categories li{padding-left:22px;position:relative}
  .categories li::before{content:"";position:absolute;left:0;top:11px;width:10px;height:10px;border-radius:50%;background:var(--ink)}

  .details{position:absolute;left:100px;top:845px;width:724px;text-align:center;color:var(--ink)}
  .sampling{font-size:16px;line-height:20px}
  .availability{font-size:20px;line-height:24px;margin-top:10px}
  .pricing{font-size:15px;line-height:19px;margin-top:10px}
  .social{font-size:13px;margin-top:10px;display:flex;align-items:center;justify-content:center;gap:8px}
  .social .dot{width:24px;height:24px;border-radius:50%;background:var(--ink)}
  .email{font-size:16px;margin-top:8px}
  .more-info{font-size:15px;margin-top:2px}

  .prize-arrow{position:absolute;left:0;top:900px;width:300px;height:160px}
  .prize-arrow text{fill:var(--white);font-family:"Montserrat",Arial,sans-serif;font-weight:800}
</style>
</head>
<body>
  <div class="newsprint-backdrop" role="img" aria-label="Faded old newspaper page texture behind the poster"></div>

  <main class="poster">
    <div class="header-band"></div>

    <svg class="slogan-block" viewBox="0 0 300 360" aria-hidden="true">
      <polygon points="0,0 262,0 292,205 230,250 0,352" fill="var(--slogan-bg)"/>
    </svg>

    <div class="slogan">
      <span class="big">Stay</span>
      <span class="big">Bright</span>
      <span class="small">Buy</span>
      <span class="big">Nearby</span>
    </div>

    <h1 class="title">
      <span class="title-year">1ST ANNUAL</span>
      <span class="title-name">Market Corner Fair</span>
    </h1>

    <p class="tagline">First of its kind in North Grenville</p>

    <div class="booth-visual" role="img" aria-label="Photo of an empty exhibition booth with curved header, screen and counter"></div>

    <div class="info-tag tag-venue">
      <svg width="415" height="54" viewBox="0 0 415 54" aria-hidden="true"><polygon points="0,0 415,0 395,54 0,54" fill="var(--tag)"/></svg>
      <span>North Grenville Municipal Centre</span>
    </div>
    <div class="info-tag tag-date">
      <svg width="295" height="54" viewBox="0 0 295 54" aria-hidden="true"><polygon points="0,0 295,0 275,54 0,54" fill="var(--tag)"/></svg>
      <span>Saturday April 18 2015</span>
    </div>
    <div class="info-tag tag-hours">
      <svg width="195" height="54" viewBox="0 0 195 54" aria-hidden="true"><polygon points="0,0 195,0 175,54 0,54" fill="var(--tag)"/></svg>
      <span>9am - 3pm</span>
    </div>

    <ul class="categories">
      <li>Home Services, Sales &amp; Renovations</li>
      <li>Local Dining and Confectionaries</li>
      <li>Healthy Active Living Services</li>
      <li>Weddings – Planning/Caterers/Decor</li>
      <li>Artisans &amp; One of a Kind Creations</li>
    </ul>

    <section class="details">
      <p class="sampling">Food, beer and wine sampling</p>
      <p class="availability">Both booths and marketplace tables are available</p>
      <p class="pricing">8' Booths available - $250 (after April 1st - $300)<br>6' Marketplace Tables available - $150</p>
      <p class="social">Like Us on Chatterbook <span class="dot"></span></p>
      <p class="email">marketcornerfair@mailbay.example</p>
      <p class="more-info">More information available on Chatterbook: Kemptville Market Corner Fair</p>
    </section>

    <svg class="prize-arrow" viewBox="0 0 300 160" aria-hidden="true">
      <polygon points="0,72 236,10 298,30 252,92 0,158" fill="var(--arrow)"/>
      <g transform="rotate(-15 20 110)">
        <text x="38" y="92" font-size="26">WIN A TRIP</text>
        <text x="20" y="132" font-size="36">FOR TWO</text>
      </g>
    </svg>
  </main>
</body>
</html>
```